my personal cards just intrducing my self

Massage Therapy to get my name out their

Target Market(s)

40 year olds who enjoy massage

Industry/Entity Type

Massage

Contact Information for Business Card

Leonard T Vasquelle
LMT-Licensed Massage Therapist
*Swedish *Deep Tissue *Prenatal
*Reflexology *Chair and more

(602)-347-2916
leonardvasquelle@mailorbit.net

Font styles to use
Serif

Colors
0456a4
6b449b

```html
<!DOCTYPE html>
<html lang="en">
<head>
<meta charset="utf-8">
<title>Leonard T Vasquelle — Business Card</title>
<link rel="stylesheet" href="https://fonts.googleapis.com/css2?family=Alfa+Slab+One&family=Questrial&display=swap">
<style>
  :root {
    --backdrop: #2b2b2b;
    --card: #f7f7f5;
    --card-edge: #e2e2df;
    --accent-blue: #1b9ad6;
    --ink: #2a2a2a;
    --ink-soft: #6e6e6e;
    --rule: #8c8c8c;
    --service-grey: #8e8e8e;
  }
  * { box-sizing: border-box; margin: 0; padding: 0; }
  html, body {
    width: 1200px; height: 900px; overflow: hidden;
    background: var(--backdrop);
  }
  .stage {
    width: 1200px; height: 900px;
    display: flex; flex-direction: column;
    align-items: center; justify-content: center; gap: 40px;
  }
  .card {
    width: 630px; height: 360px;
    background: var(--card);
    border: 1px solid var(--card-edge);
    position: relative;
    overflow: hidden;
  }
  .card-back svg { display: block; }
  .service-word {
    font-family: "Alfa Slab One", Georgia, serif;
    fill: var(--service-grey);
  }
  .card-front {
    font-family: "Questrial", "Century Gothic", sans-serif;
    color: var(--ink);
  }
  .identity {
    position: absolute; left: 60px; right: 60px; top: 58px;
    text-align: center;
  }
  .full-name {
    font-size: 34px; letter-spacing: 0.5px;
    color: var(--accent-blue); line-height: 1;
  }
  .full-name .given-name { font-family: "Alfa Slab One", Georgia, serif; font-weight: 400; }
  .full-name .surname { font-weight: 400; }
  .job-title {
    font-size: 18px; color: var(--ink-soft); margin-top: 6px;
  }
  .rule {
    position: absolute; height: 1px; background: var(--rule);
  }
  .rule-top { left: 90px; right: 90px; top: 150px; }
  .rule-mid { left: 60px; right: 60px; top: 225px; }
  .rule-bottom { left: 60px; right: 60px; top: 300px; }
  .contact-line {
    position: absolute; left: 0; right: 0;
    display: flex; align-items: center; justify-content: center; gap: 12px;
  }
  .contact-phone { top: 172px; font-size: 22px; font-weight: 700; letter-spacing: 0.5px; }
  .contact-email { top: 246px; font-size: 21px; }
  .contact-icon { flex: none; }
</style>
</head>
<body>
<main class="stage">

  <section class="card card-back" aria-label="Card back: massage services">
    <svg width="630" height="360" viewBox="0 0 630 360">
      <text class="service-word" x="28" y="92" font-size="82" textLength="400" lengthAdjust="spacingAndGlyphs">SWEDISH</text>
      <text class="service-word" x="28" y="160" font-size="64" textLength="480" lengthAdjust="spacingAndGlyphs">DEEP TISSUE</text>
      <text class="service-word" x="28" y="207" font-size="42" textLength="574" lengthAdjust="spacingAndGlyphs">PRENATAL REFLEXOLOGY</text>
      <text class="service-word" x="28" y="330" font-size="128" textLength="470" lengthAdjust="spacingAndGlyphs">SPORTS</text>
      <text class="service-word" x="512" y="250" font-size="18" textLength="92" lengthAdjust="spacingAndGlyphs">AND MORE.......</text>
    </svg>
  </section>

  <section class="card card-front" aria-label="Card front: contact details">
    <div class="identity">
      <h1 class="full-name"><span class="given-name">LEONARD</span> <span class="surname">T VASQUELLE</span></h1>
      <p class="job-title">LMT-Licensed Massage Therapist</p>
    </div>
    <div class="rule rule-top"></div>

    <p class="contact-line contact-phone">
      <svg class="contact-icon" width="16" height="16" viewBox="0 0 24 24" aria-hidden="true">
        <path fill="var(--accent-blue)" d="M6.6 10.8a15.1 15.1 0 0 0 6.6 6.6l2.2-2.2c.3-.3.7-.4 1-.2 1.1.4 2.3.6 3.6.6.6 0 1 .4 1 1V20c0 .6-.4 1-1 1A17 17 0 0 1 3 4c0-.6.4-1 1-1h3.5c.6 0 1 .4 1 1 0 1.3.2 2.5.6 3.6.1.3 0 .7-.2 1z"/>
      </svg>
      (602)-347-2916
    </p>
    <div class="rule rule-mid"></div>

    <p class="contact-line contact-email">
      <svg class="contact-icon" width="22" height="16" viewBox="0 0 22 16" aria-hidden="true">
        <rect x="0" y="0" width="22" height="16" fill="var(--accent-blue)"/>
        <path d="M1 1 L11 9 L21 1" fill="none" stroke="#ffffff" stroke-width="1.5"/>
      </svg>
      leonardvasquelle@mailorbit.net
    </p>
    <div class="rule rule-bottom"></div>
  </section>

</main>
</body>
</html>
```